Hello everyone,
I need someone to design a Business Card for my new company. It's called Nordavela and we give procurement services of Chilean Salmon and Seafood in General. More specifically we are purchasing agents, quality inspectors and we help with general papework and logistics. Maybe in the future can open to some agriculture items such as Meat, Dairy Products and Fruits.
All this focused in international clients that cannot have the support they need when buying items from Chile.
A main concept is reliability.

Thank you in advance.

Estanislao.

Target Market(s)

Salmon and Seafood Importers from all world.

Industry/Entity Type

Business

Contact Information for Business Card

The Name: Estanislao Ferrada Quiroz
My Mobile: +56 9 47315268
My Location: Puerto varas, Chile

Font styles to use
Serif
Sans Serif

Requirements
Must have
• The company name and a logo.
Nice to have
• Some full color on the back side.
Should not have
• No modern shapes. Just a rectangular business card. Remember that has to be accepted by a lot of different cultures, even senior Japanese clients.

```html
<!DOCTYPE html>
<html lang="en">
<head>
<meta charset="utf-8">
<title>Nordavela – Business Card</title>
<link rel="stylesheet" href="https://fonts.googleapis.com/css2?family=Marcellus&family=Michroma&display=swap">
<style>
  :root {
    --backdrop: #e4e5e6;
    --card: #ffffff;
    --brand-blue: #2596d1;
    --brand-grey: #9a9c9e;
    --ink: #3a3b3d;
    --ink-soft: #6b6d70;
    --rule: #b9bbbd;
  }
  html, body {
    margin: 0;
    padding: 0;
    width: 1200px;
    height: 771px;
    overflow: hidden;
    background: var(--backdrop);
  }
  .sheet {
    position: relative;
    width: 1200px;
    height: 771px;
  }
  .card {
    position: absolute;
    top: 231px;
    width: 540px;
    height: 309px;
    background: var(--card);
    box-shadow: 0 2px 10px rgba(0,0,0,0.12);
    overflow: hidden;
  }
  .card--back { left: 40px; }
  .card--front { left: 620px; }

  .wordmark {
    position: absolute;
    font-family: "Marcellus", serif;
    font-weight: 400;
    color: var(--brand-blue);
    letter-spacing: 1px;
    margin: 0;
    white-space: nowrap;
  }
  .card--back .wordmark {
    left: 0;
    right: 0;
    top: 128px;
    text-align: center;
    font-size: 46px;
  }
  .card--front .wordmark {
    left: 190px;
    top: 38px;
    font-size: 40px;
  }

  .swoosh {
    position: absolute;
    left: 0;
    top: 0;
    width: 540px;
    height: 309px;
  }

  .contact {
    position: absolute;
    top: 128px;
    left: 0;
    width: 540px;
    font-family: "Michroma", sans-serif;
    color: var(--ink);
  }
  .contact__person {
    position: absolute;
    right: 282px;
    top: 0;
    text-align: right;
    font-size: 8px;
    line-height: 13px;
    letter-spacing: 0.6px;
    text-transform: uppercase;
  }
  .contact__name {
    font-family: "Marcellus", serif;
    font-size: 12px;
    letter-spacing: 1.4px;
    color: var(--ink);
  }
  .contact__role { color: var(--ink-soft); margin-bottom: 6px; }
  .contact__address { color: var(--ink-soft); }
  .contact__divider {
    position: absolute;
    left: 266px;
    top: 0;
    width: 1px;
    height: 74px;
    background: var(--rule);
  }
  .contact__lines {
    position: absolute;
    left: 276px;
    top: 0;
    margin: 0;
    padding: 0;
    list-style: none;
    font-size: 8px;
    line-height: 15px;
    letter-spacing: 0.6px;
    color: var(--ink);
  }
  .contact__lines li {
    display: flex;
    align-items: center;
    gap: 6px;
  }
  .contact__icon {
    width: 10px;
    height: 10px;
    flex: none;
  }
</style>
</head>
<body>
<main class="sheet">

  <section class="card card--back" aria-label="Card back">
    <p class="wordmark">Nordavela</p>
  </section>

  <section class="card card--front" aria-label="Card front">
    <svg class="swoosh" viewBox="0 0 540 309" aria-hidden="true">
      <path d="M230,309 C330,298 440,282 540,268 L540,309 Z" fill="var(--brand-grey)"/>
      <path d="M248,309 C345,296 450,284 540,276" fill="none" stroke="#ffffff" stroke-width="2"/>
      <path d="M0,140 C70,205 170,270 290,309 L0,309 Z" fill="var(--brand-blue)"/>
      <path d="M0,168 C75,225 165,278 262,309" fill="none" stroke="#ffffff" stroke-width="2.5"/>
    </svg>

    <p class="wordmark">Nordavela</p>

    <div class="contact">
      <div class="contact__person">
        <div class="contact__name">Tomás Riquelme</div>
        <div class="contact__role">Owner / C.E.O</div>
        <div class="contact__address">Oficina 14, Edif. Lago,<br>PV 54100</div>
      </div>
      <div class="contact__divider"></div>
      <ul class="contact__lines">
        <li>
          <svg class="contact__icon" viewBox="0 0 10 10" aria-hidden="true"><circle cx="5" cy="5" r="5" fill="var(--ink)"/><path d="M3.2,2.6 L4.2,3.6 L3.7,4.3 C4.1,5.1 4.9,5.9 5.7,6.3 L6.4,5.8 L7.4,6.8 L6.7,7.5 C4.8,7.2 2.8,5.2 2.5,3.3 Z" fill="#fff"/></svg>
          214-530-7781
        </li>
        <li>
          <svg class="contact__icon" viewBox="0 0 10 10" aria-hidden="true"><circle cx="5" cy="5" r="5" fill="var(--ink)"/><rect x="3.5" y="2.3" width="3" height="5.4" rx="0.6" fill="#fff"/></svg>
          862-417-3095
        </li>
        <li>
          <svg class="contact__icon" viewBox="0 0 10 10" aria-hidden="true"><circle cx="5" cy="5" r="5" fill="var(--ink)"/><rect x="2.6" y="3" width="4.8" height="4" fill="#fff"/><rect x="3.4" y="2.2" width="3.2" height="1.2" fill="#fff"/></svg>
          573-208-6614
        </li>
        <li>
          <svg class="contact__icon" viewBox="0 0 10 10" aria-hidden="true"><circle cx="5" cy="5" r="5" fill="var(--ink)"/><rect x="2.4" y="3.2" width="5.2" height="3.6" fill="#fff"/><path d="M2.4,3.2 L5,5.2 L7.6,3.2" fill="none" stroke="var(--ink)" stroke-width="0.6"/></svg>
          hola@nordavela-mail.com
        </li>
        <li>
          <svg class="contact__icon" viewBox="0 0 10 10" aria-hidden="true"><circle cx="5" cy="5" r="5" fill="var(--ink)"/><circle cx="5" cy="5" r="2.6" fill="none" stroke="#fff" stroke-width="0.7"/><path d="M2.4,5 H7.6 M5,2.4 V7.6" stroke="#fff" stroke-width="0.6"/></svg>
          www.nordavela-web.com
        </li>
      </ul>
    </div>
  </section>

</main>
</body>
</html>
```